New Website for ReBranded Company - CrewBeacon

We have a successful company and website currently but it is a little dated. We have re-branded the company from Harbor Signal Networks to CrewBeacon and have a new logo for the new name. We are looking to build a newer fresher website with the new name. I will need a concept of the home page and one inside page. You can see our current site at https://www.harborsignalnetworks.example and the new site will be https://www.crewbeacon.example .

I also really like the https://www.pathlantern.example/ website. I like ledgerkite.example website. I like the https://skillorbit.example/ website.

See the attached document for layout and some text to use. Use the pictures I attached as opposed to pictures from the old site as much as you can.

Target Market(s)

Business

Industry/Entity Type

Software Service

Number of Pages Required

2 page

Font styles to use
Sans Serif

Requirements
Must have
• Use the colors from my logo. Professional but modern. We want people to feel like our product makes their staff feel safer at work.
Should not have
• Don't use any red or orange (no stop colors).

```html
<!DOCTYPE html>
<html lang="en">
<head>
<meta charset="utf-8">
<title>CrewBeacon — Feel Confident That Your Staff Is Protected</title>
<link rel="stylesheet" href="https://fonts.googleapis.com/css2?family=Montserrat:wght@400;500;600;700;800&family=Poppins:wght@400;500;600;700&display=swap">
<style>
:root{
  --green:#7cc242;
  --green-dark:#5fa32b;
  --navy:#1f3a5c;
  --indigo:#23236b;
  --sky:#3aa0dc;
  --ink:#2c3440;
  --muted:#6b7480;
  --ghost:#eef1f5;
  --footer:#1a2230;
  --white:#ffffff;
}
*{box-sizing:border-box;margin:0;padding:0}
html,body{width:1200px;height:4248px;overflow:hidden}
body{font-family:"Poppins",sans-serif;color:var(--ink);background:var(--white);position:relative}
.abs{position:absolute}
.btn{display:inline-block;background:var(--green);color:var(--white);font-family:"Montserrat",sans-serif;font-weight:600;font-size:15px;padding:13px 30px;border-radius:3px}
.photo{position:absolute;left:0;width:1200px}
.wave{position:absolute;left:0;width:1200px}
.chev{position:absolute;left:570px;width:60px;height:60px;border-radius:50%;background:var(--white);box-shadow:0 4px 12px rgba(0,0,0,.15);display:flex;align-items:center;justify-content:center}

/* hero */
.hero-photo{top:0;height:600px;background:linear-gradient(180deg,#3b4552 0%,#59616c 55%,#7b7f86 100%)}
.hero-shade{position:absolute;top:0;left:0;width:1200px;height:600px;background:rgba(20,28,40,.55)}
.nav{top:20px;left:200px;width:800px;height:44px;display:flex;align-items:center;justify-content:space-between}
.brand{display:flex;align-items:center;gap:10px;font-family:"Montserrat",sans-serif;font-weight:700;font-size:22px;color:var(--white)}
.brand-dot{width:28px;height:28px;border-radius:50%;background:var(--green)}
.nav-links{display:flex;align-items:center;gap:34px;font-size:13px;color:var(--white)}
.nav-links .active{color:var(--green)}
.nav-links .btn{font-size:12px;padding:9px 18px}
.hero-title{top:148px;left:0;width:1200px;text-align:center;font-family:"Montserrat",sans-serif;font-weight:800;font-size:42px;line-height:1.2;color:var(--white);text-transform:uppercase}
.hero-sub{top:298px;width:1200px;text-align:center;font-size:22px;color:var(--white)}
.hero-btn{top:368px;left:0;width:1200px;text-align:center}
.dots{top:455px;left:0;width:1200px;display:flex;justify-content:center;gap:10px}
.dots span{width:9px;height:9px;border-radius:50%;background:rgba(255,255,255,.5)}
.dots span.on{background:var(--white)}

/* section headings */
.ghost{left:0;width:1200px;text-align:center;font-family:"Montserrat",sans-serif;font-weight:800;font-size:84px;color:var(--ghost);text-transform:uppercase;letter-spacing:2px}
.heading{left:0;width:1200px;text-align:center;font-family:"Montserrat",sans-serif;font-weight:800;font-size:32px;color:var(--navy);text-transform:uppercase}

/* how it works */
.how-cards{top:888px;left:192px;width:816px;height:250px;display:flex;background:var(--white);box-shadow:0 6px 24px rgba(0,0,0,.1)}
.how-card{flex:1;border-right:1px solid #e3e7ec;text-align:center;padding:42px 28px 0}
.how-card:last-child{border-right:none}
.how-card p{margin-top:22px;font-size:15px;font-weight:600;color:var(--navy);line-height:1.5}

/* alone section */
.alone-photo{top:1140px;height:560px;background:linear-gradient(120deg,#2d3440 0%,#4b525d 50%,#6a6e74 100%)}
.alone-shade{position:absolute;top:1140px;left:0;width:1200px;height:560px;background:rgba(15,22,34,.5)}
.alone-title{top:1236px;left:0;width:1200px;text-align:center;font-family:"Montserrat",sans-serif;font-weight:800;font-size:38px;line-height:1.25;color:var(--white);text-transform:uppercase}
.alone-text{top:1384px;left:0;width:1200px;text-align:center;font-size:19px;line-height:1.55;color:var(--white)}
.alone-btn{top:1480px;left:0;width:1200px;text-align:center}

/* why choose us */
.why-card{background:var(--white);box-shadow:0 6px 22px rgba(0,0,0,.1);text-align:center;padding:34px 24px}
.why-card h3{font-family:"Montserrat",sans-serif;font-weight:700;font-size:15px;color:var(--navy);text-transform:uppercase;margin:18px 0 14px;line-height:1.35}
.why-card p{font-size:12.5px;line-height:1.6;color:var(--muted)}
.icon-ring{width:62px;height:62px;border-radius:50%;border:2px solid var(--sky);margin:0 auto;display:flex;align-items:center;justify-content:center}
.channels{display:grid;grid-template-columns:1fr 1fr;gap:6px 14px;text-align:left;font-size:12.5px;color:var(--muted);margin-top:14px;padding-left:20px}
.channels li{list-style:disc}
.why-btn{top:2396px;left:0;width:1200px;text-align:center}

/* coverage */
.team-photo{top:2512px;height:528px;background:linear-gradient(135deg,#8b7f75 0%,#a79a8e 40%,#6f6a67 100%)}
.team-shade{position:absolute;top:2512px;left:0;width:1200px;height:528px;background:rgba(30,30,40,.25)}
.scary-box{top:2560px;left:208px;width:392px;height:420px;background:var(--green);padding:44px 40px;color:var(--white)}
.scary-box h3{font-family:"Montserrat",sans-serif;font-weight:700;font-size:28px;line-height:1.35;margin:26px 0 30px}
.btn-white{display:inline-block;background:var(--white);color:var(--navy);font-family:"Montserrat",sans-serif;font-weight:600;font-size:14px;padding:12px 26px;border-radius:3px}
.reach-box{top:2640px;left:600px;width:392px;height:440px;background:var(--navy);padding:44px 40px;color:var(--white)}
.reach-box h3{font-family:"Montserrat",sans-serif;font-weight:700;font-size:28px;line-height:1.35}
.reach-stats{display:flex;align-items:center;margin-top:34px;gap:16px}
.covering{writing-mode:vertical-rl;transform:rotate(180deg);font-size:13px;letter-spacing:2px;opacity:.8}
.reach-stats strong{display:block;font-family:"Montserrat",sans-serif;font-weight:700;font-size:38px;line-height:1.25}

/* plan */
.plan-title{top:3110px;left:190px;font-family:"Montserrat",sans-serif;font-weight:800;font-size:62px;line-height:1.1;color:var(--indigo);text-transform:uppercase}
.steps{top:3310px;left:190px;width:820px;display:flex;gap:28px}
.step{flex:1;display:flex;gap:12px}
.step-num{font-family:"Montserrat",sans-serif;font-weight:700;font-size:72px;line-height:.9;color:var(--sky)}
.step-card{flex:1;background:var(--white);box-shadow:0 6px 20px rgba(0,0,0,.1);padding:20px 18px;min-height:180px}
.step-card h4{font-size:14.5px;font-weight:600;color:var(--sky);line-height:1.35;margin-bottom:10px}
.step-card li{list-style:none;font-size:12.5px;color:var(--muted);line-height:1.8}
.step-card li::before{content:"• ";color:var(--green)}
.step-card p{font-size:12.5px;color:var(--muted);line-height:1.6}

/* cta */
.cta-photo{top:3520px;height:460px;background:linear-gradient(160deg,#4a4f58 0%,#6d6a68 50%,#3c414a 100%)}
.cta-shade{position:absolute;top:3520px;left:0;width:1200px;height:460px;background:rgba(15,22,34,.55)}
.cta-title{top:3700px;left:0;width:1200px;text-align:center;font-family:"Montserrat",sans-serif;font-weight:600;font-size:36px;color:var(--white)}
.cta-btn{top:3786px;left:0;width:1200px;text-align:center}

/* footer */
.footer{top:3980px;left:0;width:1200px;height:268px;background:var(--footer);color:#c8cfd9}
.foot-about{position:absolute;top:44px;left:190px;width:240px}
.foot-about p{font-size:11.5px;line-height:1.6;margin:14px 0 12px}
.foot-call{font-family:"Montserrat",sans-serif;font-weight:700;font-size:18px;color:var(--white)}
.foot-phone{font-family:"Montserrat",sans-serif;font-weight:700;font-size:17px;color:var(--green)}
.foot-col{position:absolute;top:50px}
.foot-col h5{font-family:"Montserrat",sans-serif;font-weight:700;font-size:15px;color:var(--white);text-transform:uppercase;margin-bottom:12px}
.foot-col li{list-style:none;font-size:12px;line-height:1.75}
.socials{display:flex;gap:8px;margin-top:40px}
.socials span{width:22px;height:22px;background:#3a4558;border-radius:3px}
.copy{position:absolute;top:236px;left:880px;font-size:10px;color:#7d8796}
</style>
</head>
<body>

<!-- hero -->
<div class="photo hero-photo" role="img" aria-label="Team of colleagues working together at desks in a bright office"></div>
<div class="hero-shade"></div>
<nav class="abs nav">
  <div class="brand"><span class="brand-dot"></span>CrewBeacon</div>
  <div class="nav-links">
    <span class="active">Home</span>
    <span>Buy Button</span>
    <span>Login</span>
    <span class="btn">Register Your Company</span>
  </div>
</nav>
<h1 class="abs hero-title">Feel Confident That Your<br>Staff Is Protected</h1>
<p class="abs hero-sub">Get a revolutionary new electronic panic button</p>
<div class="abs hero-btn"><span class="btn">Ready To Get Started</span></div>
<div class="abs dots"><span></span><span class="on"></span><span></span><span></span></div>
<svg class="wave" style="top:520px" width="1200" height="82" viewBox="0 0 1200 82" aria-hidden="true">
  <path d="M0 82 Q600 -10 1200 82 Z" fill="#fff"/>
  <path d="M0 70 Q600 -20 1200 70" fill="none" stroke="#1f3a5c" stroke-width="6"/>
</svg>
<div class="chev" style="top:566px"><svg width="22" height="14" viewBox="0 0 22 14"><path d="M2 2 L11 11 L20 2" fill="none" stroke="#3aa0dc" stroke-width="3"/></svg></div>

<!-- how it works -->
<div class="abs ghost" style="top:664px">How It Works</div>
<h2 class="abs heading" style="top:758px">How It Works</h2>
<div class="abs how-cards">
  <div class="how-card">
    <svg width="56" height="56" viewBox="0 0 56 56"><circle cx="28" cy="28" r="25" fill="none" stroke="#3aa0dc" stroke-width="3"/><path d="M16 29 L25 38 L41 20" fill="none" stroke="#7cc242" stroke-width="4"/></svg>
    <p>Problems Stopped Before They Start For Any Type Of Organization</p>
  </div>
  <div class="how-card">
    <svg width="56" height="56" viewBox="0 0 56 56"><circle cx="28" cy="28" r="25" fill="none" stroke="#3aa0dc" stroke-width="3"/><text x="28" y="37" text-anchor="middle" font-family="Montserrat,sans-serif" font-weight="700" font-size="26" fill="#7cc242">$</text></svg>
    <p>Affordable Prices Starting At $18 Per Month. No Contracts, No Hidden Costs.</p>
  </div>
  <div class="how-card">
    <svg width="56" height="56" viewBox="0 0 56 56"><circle cx="28" cy="28" r="25" fill="none" stroke="#3aa0dc" stroke-width="3"/><rect x="20" y="13" width="16" height="30" rx="3" fill="none" stroke="#7cc242" stroke-width="3"/><circle cx="28" cy="38" r="1.8" fill="#7cc242"/></svg>
    <p>Access By Computer, Mobile Device, Text, Phone, Email, Monitoring And 24/7</p>
  </div>
</div>

<!-- alone -->
<div class="photo alone-photo" role="img" aria-label="Empty office meeting room with chairs and a conference phone"></div>
<div class="alone-shade"></div>
<h2 class="abs alone-title">Your Empoyees Shouldn't Feel<br>Alone When They Need Help.</h2>
<p class="abs alone-text">Does this problem make you feel frustrated and anxious?<br>Put a simple solution in their hands.</p>
<div class="abs alone-btn"><span class="btn">Ready To Get Started</span></div>
<svg class="wave" style="top:1620px" width="1200" height="82" viewBox="0 0 1200 82" aria-hidden="true">
  <path d="M0 82 Q600 -10 1200 82 Z" fill="#fff"/>
  <path d="M0 70 Q600 -20 1200 70" fill="none" stroke="#1f3a5c" stroke-width="6"/>
</svg>
<div class="chev" style="top:1666px"><svg width="22" height="14" viewBox="0 0 22 14"><path d="M2 2 L11 11 L20 2" fill="none" stroke="#3aa0dc" stroke-width="3"/></svg></div>

<!-- why choose us -->
<div class="abs ghost" style="top:1736px;font-size:70px">Why Businesses Choose Us</div>
<h2 class="abs heading" style="top:1812px">Why Choose Us</h2>
<div class="abs why-card" style="top:1918px;left:220px;width:240px;height:330px">
  <div class="icon-ring"><svg width="26" height="34" viewBox="0 0 26 34"><rect x="3" y="2" width="20" height="30" rx="3" fill="none" stroke="#3aa0dc" stroke-width="2.5"/><circle cx="13" cy="26" r="2" fill="#3aa0dc"/></svg></div>
  <h3>The Device Is Really Easy To Use</h3>
  <p>Press a button and let the right people know you need help fast. Clear alerts reach the team right away, with no setup or training needed for your staff.</p>
</div>
<div class="abs why-card" style="top:1890px;left:480px;width:260px;height:380px">
  <div class="icon-ring"><svg width="30" height="26" viewBox="0 0 30 26"><path d="M3 3 H27 V18 H12 L6 23 V18 H3 Z" fill="none" stroke="#3aa0dc" stroke-width="2.5" stroke-linejoin="round"/></svg></div>
  <h3>Communicate The Way<br>You Want</h3>
  <p>We give you a range of options to stay connected:</p>
  <ul class="channels">
    <li>Computer</li><li>Text</li>
    <li>Mobile</li><li>Email</li>
    <li>Phone</li><li>Call Center</li>
    <li>Phone Link</li>
  </ul>
</div>
<div class="abs why-card" style="top:1918px;left:760px;width:240px;height:330px">
  <div class="icon-ring"><svg width="26" height="30" viewBox="0 0 26 30"><rect x="3" y="13" width="20" height="15" rx="2" fill="none" stroke="#3aa0dc" stroke-width="2.5"/><path d="M7 13 V9 a6 6 0 0 1 12 0 V13" fill="none" stroke="#3aa0dc" stroke-width="2.5"/></svg></div>
  <h3>Cost Effective Protection</h3>
  <p>By using your existing network and equipment we can lower your costs. It's a better option for keeping your staff safe.</p>
</div>
<div class="abs why-btn"><span class="btn">Ready To Get Started</span></div>

<!-- coverage -->
<div class="photo team-photo" role="img" aria-label="Colleagues seated around a table in a casual team meeting"></div>
<div class="team-shade"></div>
<div class="abs scary-box">
  <svg width="50" height="50" viewBox="0 0 50 50" aria-hidden="true"><circle cx="25" cy="25" r="22" fill="none" stroke="#fff" stroke-width="3"/></svg>
  <h3>We Know How Scary It Can Feel To Worry About Employee Safety.</h3>
  <span class="btn-white">Start My Demo</span>
</div>
<div class="abs reach-box">
  <h3>That's Why We Have Provided A Way For Customers To Get Help To Staff Effectively In</h3>
  <div class="reach-stats">
    <span class="covering">Covering</span>
    <div><strong>45 States</strong><strong>5 Countries</strong></div>
  </div>
</div>

<!-- plan -->
<h2 class="abs plan-title">Simple<br>Start Plan</h2>
<div class="abs steps">
  <div class="step">
    <span class="step-num">1</span>
    <div class="step-card">
      <h4>Explore Your Choices</h4>
      <ul><li>Pricing</li><li>Trial</li><li>Guide</li><li>Hardware</li></ul>
    </div>
  </div>
  <div class="step">
    <span class="step-num">2</span>
    <div class="step-card">
      <h4>Get Setup</h4>
      <ul><li>Input Your Alerts</li><li>Input Your Staff</li><li>Install Your Software</li></ul>
    </div>
  </div>
  <div class="step">
    <span class="step-num">3</span>
    <div class="step-card">
      <h4>Feel Confident Your Staff Is Protected</h4>
      <p>High Five. You Just Took A Major Step To Getting Rid Of The Anxiety And Frustration This Gave You.</p>
    </div>
  </div>
</div>

<!-- cta -->
<div class="photo cta-photo" role="img" aria-label="Staff members talking together in a modern office"></div>
<div class="cta-shade"></div>
<svg class="wave" style="top:3518px" width="1200" height="90" viewBox="0 0 1200 90" aria-hidden="true">
  <path d="M0 0 H1200 V10 Q600 120 0 10 Z" fill="#fff"/>
</svg>
<h2 class="abs cta-title">Stay Connected with Staff during a Crisis Situations</h2>
<div class="abs cta-btn"><span class="btn">Start My Demo</span></div>

<!-- footer -->
<footer class="abs footer">
  <div class="foot-about">
    <div class="brand" style="font-size:20px"><span class="brand-dot" style="width:24px;height:24px"></span>CrewBeacon</div>
    <p>When employees feel alone during a threatening situation, we give them a way to call for help quickly so your team can feel confident at work.</p>
    <div class="foot-call">Call Us</div>
    <div class="foot-phone">1 - 800 - 555 - 0142</div>
  </div>
  <div class="foot-col" style="left:500px">
    <h5>Quick Links</h5>
    <ul><li>About Us</li><li>Contact Us</li><li>Support</li><li>Training</li><li>Community</li><li>Blog</li><li>FAQ</li></ul>
  </div>
  <div class="foot-col" style="left:700px">
    <h5>Shop</h5>
    <ul><li>Get Plan</li><li>Start My Demo</li><li>Custom Quote</li><li>Start Trial</li></ul>
  </div>
  <div class="foot-col" style="left:880px">
    <h5>Legal</h5>
    <ul><li>Privacy Policy</li><li>Terms Of Use</li><li>End User License</li><li>Agreement</li></ul>
    <div class="socials"><span></span><span></span><span></span><span></span></div>
  </div>
  <div class="copy">© CrewBeacon 2024</div>
</footer>

</body>
</html>
```